Valmora Building Company Portfolio Design

I need a full design for a Company Portfolio for a Kuwait based company called Valmora Building Company, WLL. We offer services in Construction ( Supply of Construction Machinery & Construction Material), Contracting (Steel Structure, Furnishing & Finishing) and Smart Solutions (Smart Homes & Smart Parking).

https://www.filetarn.example/s/qpzk4vn82tmhdwe/Photos.zip

This is a File Tarn Link containing all our images that can be used in the Company Profile.

One or more of each can be more than enough to describe each product or service we provide.

Target Market(s)

Construction Companies, Engineering & Design Companies, Consultancy firms.

Industry/Entity Type

Construction

Requirements
Must have
• 1) Must allow for further addition & modification.
Nice to have
• 1) External Photos can be used for a better look & resolution.

```html
<!DOCTYPE html>
<html lang="en">
<head>
<meta charset="utf-8">
<title>Valmora Building Company — Portfolio Cover</title>
<link rel="stylesheet" href="https://fonts.googleapis.com/css2?family=Jost:wght@300;700&display=swap">
<style>
  :root {
    --teal: #0e8283;
    --teal-deep: #0a6a6b;
    --white: #ffffff;
    --ink: #1d1d1b;
    --sky: #b9c4cc;
    --steel: #6f7c86;
  }
  * { margin: 0; padding: 0; box-sizing: border-box; }
  html, body { width: 848px; height: 1200px; overflow: hidden; background: var(--white); }
  .cover {
    position: relative;
    width: 848px;
    height: 1200px;
    background: var(--teal);
    font-family: "Jost", "Futura", sans-serif;
    color: var(--white);
    overflow: hidden;
  }
  .hero-visual {
    position: absolute;
    left: 88px;
    top: -60px;
    width: 680px;
    height: 640px;
    border-radius: 50%;
    background:
      radial-gradient(ellipse at 50% 55%,
        #e8edf0 0%, var(--sky) 30%, var(--steel) 50%,
        rgba(14,130,131,0.6) 62%, rgba(14,130,131,0) 71%);
  }
  .headline {
    position: absolute;
    left: 0;
    top: 600px;
    width: 848px;
    line-height: 1;
  }
  .headline span { position: absolute; white-space: nowrap; }
  .light { font-weight: 300; }
  .bold { font-weight: 700; }
  .line-leading { left: 285px; top: 0; font-size: 62px; }
  .line-construction { left: 212px; top: 62px; font-size: 74px; letter-spacing: -0.5px; }
  .line-trading { left: 285px; top: 140px; font-size: 58px; }
  .line-company { left: 212px; top: 190px; font-size: 74px; letter-spacing: -0.5px; }
  .line-kuwait { left: 262px; top: 262px; font-size: 72px; }
  .line-kuwait .bold { position: static; }
  .brand-band {
    position: absolute;
    left: 0;
    bottom: 0;
    width: 848px;
    height: 202px;
    background: var(--white);
  }
  .brand {
    position: absolute;
    right: 52px;
    top: 70px;
    display: flex;
    align-items: center;
    gap: 18px;
  }
  .brand-square {
    width: 40px;
    height: 40px;
    background: var(--teal);
  }
  .brand-name {
    font-weight: 700;
    font-size: 31px;
    line-height: 1.05;
    color: var(--ink);
    letter-spacing: 1px;
    text-transform: uppercase;
  }
</style>
</head>
<body>
  <main class="cover">
    <div class="hero-visual" role="img" aria-label="Construction image: two glass office towers under construction with yellow tower cranes over architectural blueprints"></div>

    <h1 class="headline">
      <span class="line-leading light">Leading</span>
      <span class="line-construction bold">Construction</span>
      <span class="line-trading light">and Trading</span>
      <span class="line-company bold">Company</span>
      <span class="line-kuwait light">in <span class="bold">Kuwait</span></span>
    </h1>

    <footer class="brand-band">
      <div class="brand">
        <div class="brand-square"></div>
        <div class="brand-name">Valmora<br>Building Company</div>
      </div>
    </footer>
  </main>
</body>
</html>
```